Asian Pakistani: Wedding Invitation

Design a pakistani asian wedding invitation.
Islamic theme, with arabic text:

Text to be used:

Start with: bismillah and dua for marriage. (The Holy Quran chapter 25 verse 75 with arabic text and english translation below)

Mrs. Rubina Sohail wife of (late) Mr. Sohail Imran Qureshi
Cordially requests your company to grace the joyous occasion of the wedding of their beloved daughter
Mehreen Qureshi
Daughter of ( late) Mr Sohail Imran qureshi
with
Bilal Siddiqui
Son of Mr. Junaid Siddiqui & Mrs Shazia Siddiqui

Insha’Allah on Thursday 29th August 2019 at Velvet Orchard
12 Marlow Crescent, Croydon
CR7 2LP
Baraat Arrival 6:30

RSVP
Usman Qureshi 07700 900412
Tariq Mehmood 07700 900583
Faisal Butt 07700 900735

Target Market(s)

Muslims

Font styles to use
Script

Colors

Designer to choose colors to be used in the design.

Requirements
Must have
• stylish calligraphy Arabic lettering of the dua requested above
• Size:
• Long 4" x 9.5"
Nice to have
• ottoman empire: Art theme

```html
<!DOCTYPE html>
<html lang="en">
<head>
<meta charset="utf-8">
<title>Wedding Invitation</title>
<link href="https://fonts.googleapis.com/css2?family=Playball&family=Tinos:ital,wght@0,400;0,700;1,400&display=swap" rel="stylesheet">
<style>
  :root{
    --backdrop:#4a4a4c;
    --card:#ffffff;
    --mist:#eef0f3;
    --navy:#1b3a5c;
    --navy-deep:#12304f;
    --gold:#f2c40f;
    --ink:#1f2f45;
    --white:#ffffff;
    --rule:#c9d2dd;
  }
  *{box-sizing:border-box;margin:0;padding:0}
  html,body{width:1200px;height:2356px;overflow:hidden}
  body{background:var(--backdrop);position:relative;font-family:"Tinos",serif;color:var(--ink)}
  .invitation{position:absolute;left:160px;top:128px;width:880px;height:2096px;background:linear-gradient(var(--mist),var(--card) 30%,var(--card) 80%,var(--mist));overflow:hidden}
  .ornament{position:absolute;border-radius:50%;background:radial-gradient(circle,rgba(27,58,92,.22),rgba(201,210,221,.25) 55%,rgba(255,255,255,0) 72%)}
  .ornament--tr{right:-150px;top:-110px;width:420px;height:420px}
  .ornament--mr{right:-170px;top:330px;width:400px;height:400px}
  .ornament--ml{left:-170px;top:1420px;width:400px;height:400px}
  .ornament--bl{left:-140px;bottom:-160px;width:440px;height:440px}
  .bismillah{position:absolute;left:200px;top:140px;width:480px;height:96px;border-radius:40px;background:linear-gradient(90deg,rgba(27,58,92,.25),rgba(27,58,92,.85),rgba(27,58,92,.25))}
  .center{position:absolute;left:0;width:100%;text-align:center}
  .bismillah-en{top:244px;font-size:31px;color:var(--navy-deep)}
  .finial{position:absolute;left:380px;width:120px;height:64px;background:radial-gradient(ellipse,rgba(27,58,92,.8),rgba(27,58,92,.15) 70%,transparent)}
  .finial--top{top:376px}
  .finial--bottom{top:852px}
  .dua-panel{position:absolute;left:220px;top:440px;width:440px;height:412px;background:var(--navy-deep);border-radius:6px}
  .dua-calligraphy{position:absolute;left:34px;top:30px;width:372px;height:170px;border-radius:30px;background:linear-gradient(90deg,rgba(255,255,255,.15),rgba(255,255,255,.55),rgba(255,255,255,.15))}
  .verse-medallion{position:absolute;left:194px;top:212px;width:52px;height:52px;border-radius:50%;border:2px solid rgba(255,255,255,.8);color:var(--white);font-size:22px;display:flex;align-items:center;justify-content:center}
  .dua-translation{position:absolute;left:22px;top:288px;width:396px;text-align:center;color:var(--white);font-size:17px;line-height:1.35}
  .hosts{top:928px;font-size:24px;font-weight:700;color:var(--navy-deep)}
  .request{top:966px;font-size:29px;line-height:1.3;color:var(--navy-deep)}
  .family-band{position:absolute;left:0;top:1064px;width:100%;height:344px;background:var(--gold)}
  .script{font-family:"Playball",cursive}
  .name{font-size:54px;color:var(--navy-deep);line-height:1.1}
  .band-text{font-size:30px;color:var(--navy-deep)}
  .bride{top:1084px}
  .bride-parent{top:1158px}
  .with{top:1212px}
  .groom{top:1254px}
  .groom-parents{top:1330px}
  .insha{top:1482px;font-size:40px;color:var(--navy-deep)}
  .date{top:1542px;font-size:33px;font-weight:700;color:var(--navy-deep)}
  .address{top:1592px;font-size:32px;line-height:52px;color:var(--navy-deep)}
  .address strong{font-weight:700}
  .rsvp{top:1826px;font-size:46px;color:var(--navy-deep);letter-spacing:4px}
  .rsvp-contacts{position:absolute;left:100px;top:1914px;width:680px;display:flex}
  .contact{flex:1;text-align:center;font-size:24px;line-height:1.6;color:var(--navy-deep);border-left:2px solid var(--rule)}
  .contact:first-child{border-left:none}
  .contact .phone{font-weight:700}
</style>
</head>
<body>
<main class="invitation">
  <div class="ornament ornament--tr" role="img" aria-label="Faint floral mandala ornament"></div>
  <div class="ornament ornament--mr" role="img" aria-label="Faint floral mandala ornament"></div>
  <div class="ornament ornament--ml" role="img" aria-label="Faint floral mandala ornament"></div>
  <div class="ornament ornament--bl" role="img" aria-label="Faint floral mandala ornament"></div>

  <div class="bismillah" role="img" aria-label="Arabic calligraphy of Bismillah ir-Rahman ir-Raheem"></div>
  <p class="center bismillah-en">In the name of Allah, the most Gracious, most Merciful</p>

  <div class="finial finial--top" role="img" aria-label="Ottoman style finial ornament"></div>
  <section class="dua-panel">
    <div class="dua-calligraphy" role="img" aria-label="Arabic calligraphy of Surah Al-Furqan verse 75"></div>
    <div class="verse-medallion">٧٥</div>
    <p class="dua-translation">Our Lord, Grant us of our Wives and Children the delight of our Eyes, and make us a Model of the righteous<br>(Sura Al-Furqan:75)</p>
  </section>
  <div class="finial finial--bottom" role="img" aria-label="Ottoman style finial ornament"></div>

  <p class="center hosts">Mrs. Rubina Sohail wife of (late) Mr. Sohail Imran Qureshi</p>
  <p class="center request">Cordially requests your company to grace the joyous<br>occasion of the wedding of their beloved daughter</p>

  <section class="family-band"></section>
  <p class="center script name bride">Mehreen Qureshi</p>
  <p class="center band-text bride-parent">Daughter of ( late) Mr Sohail Imran qureshi</p>
  <p class="center band-text with">with</p>
  <p class="center script name groom">Bilal Siddiqui</p>
  <p class="center band-text groom-parents">Son of Mr. Junaid Siddiqui &amp; Mrs Shazia Siddiqui</p>

  <p class="center script insha">Insha’Allah on Thursday</p>
  <p class="center date">29th August 2019 at Velvet Orchard</p>
  <p class="center address">12 Marlow Crescent, Croydon<br>CR7 2LP<br><strong>Baraat Arrival 6:30</strong></p>

  <p class="center script rsvp">RSVP</p>
  <section class="rsvp-contacts">
    <div class="contact">Usman Qureshi<br><span class="phone">07700 900412</span></div>
    <div class="contact">Tariq Mehmood<br><span class="phone">07700 900583</span></div>
    <div class="contact">Faisal Butt<br><span class="phone">07700 900735</span></div>
  </section>
</main>
</body>
</html>
```